Accounting firm needs a postcard design

We need a postcard design for our accounting office for a advertising campaign mailing we do yearly from a mail list we create. We are a full-service accounting office that has been in business for 35 years. I have attached our logo in different formats along with a document with a description of the services we provide. I have also attached my business card and the business card of our CPA. The business cards will have contact information for the postcard design. The contact email that will need to be on the postcard is contact@harrowledgerworks.com.

```html
<!DOCTYPE html>
<html lang="en">
<head>
<meta charset="utf-8">
<title>Harrow Ledgerworks Postcard</title>
<link rel="stylesheet" href="https://fonts.googleapis.com/css2?family=Open+Sans:wdth,wght@75..100,400..800&display=swap">
<style>
  :root {
    --navy: #1b4483;
    --green: #2e8425;
    --lime: #7dc242;
    --ink: #3a3a3a;
    --rule: #cfe0c8;
    --page: #e8e8e8;
    --paper: #ffffff;
    --photo-light: #dfe9cf;
    --photo-warm: #e6d3c2;
  }
  * { box-sizing: border-box; margin: 0; padding: 0; }
  html, body { width: 1200px; height: 1096px; overflow: hidden; background: var(--page); }
  body { position: relative; font-family: "Open Sans", sans-serif; }

  .postcard {
    position: absolute; width: 470px; height: 313px;
    background: var(--paper); overflow: hidden;
    box-shadow: 0 4px 12px rgba(0,0,0,.18);
  }
  .postcard--address { left: 99px; top: 225px; }
  .postcard--services { left: 615px; top: 585px; }

  .footer-band { position: absolute; left: 0; bottom: 0; width: 470px; height: 26px; }
  .footer-url {
    position: absolute; left: 21px; bottom: 7px;
    color: #fff; font-weight: 700; font-size: 9.5px; letter-spacing: .1px;
  }

  /* Address side */
  .brand {
    position: absolute; left: 16px; top: 92px; width: 192px; text-align: center;
  }
  .brand-name {
    color: var(--navy); font-weight: 700; font-size: 11px; letter-spacing: 1px;
    text-transform: uppercase; white-space: nowrap;
    display: flex; align-items: center; justify-content: center; gap: 6px;
  }
  .brand-mark { width: 7px; height: 7px; border-radius: 50%; background: var(--green); flex: none; }
  .brand-tagline { margin-top: 3px; color: var(--navy); font-size: 5.2px; letter-spacing: .2px; white-space: nowrap; }

  .contact-list { position: absolute; left: 21px; top: 184px; list-style: none; }
  .contact-item {
    display: flex; align-items: center; gap: 11px; color: var(--green);
    font-size: 10.5px; line-height: 15px; margin-bottom: 7px; white-space: nowrap;
  }
  .contact-item svg { width: 15px; height: 15px; flex: none; }

  .address-lines { position: absolute; left: 278px; top: 185px; width: 173px; }
  .address-line { height: 18.5px; border-top: 1px solid var(--rule); }

  /* Services side */
  .headline {
    position: absolute; left: 21px; top: 13px; color: #fff;
    font-weight: 800; font-size: 11.6px; line-height: 13.8px;
  }
  .service-column { position: absolute; left: 21px; top: 76px; width: 206px; }
  .service { margin-bottom: 6px; }
  .service-title {
    color: var(--green); font-stretch: 75%; font-weight: 700; font-size: 10.5px;
    line-height: 14px; text-transform: uppercase;
  }
  .service-text {
    color: var(--ink); font-stretch: 75%; font-size: 7.7px; line-height: 11.6px;
  }
  .service--payroll { position: absolute; left: 290px; top: 189px; width: 155px; margin: 0; }
  .service--payroll .service-title,
  .service--payroll .service-text { color: #fff; }

  .photo {
    position: absolute; left: 231px; top: 0; width: 239px; height: 172px;
    background: linear-gradient(160deg, var(--photo-light), var(--photo-warm));
  }
</style>
</head>
<body>

<section class="postcard postcard--address">
  <div class="brand">
    <div class="brand-name"><span class="brand-mark"></span>Harrow Ledgerworks</div>
    <div class="brand-tagline">Tax Preparation &nbsp;|&nbsp; Bookkeeping &nbsp;|&nbsp; Payroll &nbsp;|&nbsp; Entity Formation</div>
  </div>

  <ul class="contact-list">
    <li class="contact-item">
      <svg viewBox="0 0 16 16" aria-hidden="true"><rect x="1" y="3" width="14" height="10" fill="none" stroke="#2e8425" stroke-width="1.6"/><path d="M1 3l7 6 7-6M1 13l5-5M15 13l-5-5" fill="none" stroke="#2e8425" stroke-width="1.4"/></svg>
      contact@harrowledgerworks.com
    </li>
    <li class="contact-item">
      <svg viewBox="0 0 16 16" aria-hidden="true"><path d="M3.5 1.5l2.6 0 1 3.4-1.8 1.3c.9 2 2.4 3.5 4.4 4.4l1.3-1.8 3.4 1v2.6c0 .8-.7 1.4-1.5 1.4C6.6 13.8 2.2 9.4 2.1 3c0-.8.6-1.5 1.4-1.5z" fill="#2e8425"/></svg>
      (555)014-2290
    </li>
    <li class="contact-item">
      <svg viewBox="0 0 16 16" aria-hidden="true"><path d="M8 1a5 5 0 0 0-5 5c0 3.8 5 9 5 9s5-5.2 5-9a5 5 0 0 0-5-5zm0 7a2 2 0 1 1 0-4 2 2 0 0 1 0 4z" fill="#2e8425"/></svg>
      <span>48 Fenwick Row, Suite 310<br>Marlow, TX 75010</span>
    </li>
  </ul>

  <div class="address-lines">
    <div class="address-line"></div><div class="address-line"></div><div class="address-line"></div>
    <div class="address-line"></div><div class="address-line"></div><div class="address-line"></div>
  </div>

  <svg class="footer-band" viewBox="0 0 470 26" aria-hidden="true">
    <rect width="470" height="26" fill="var(--green)"/>
    <path d="M0 0H195C180 2 175 26 150 26H0Z" fill="var(--navy)"/>
  </svg>
  <div class="footer-url">www.harrowledgerworks.com</div>
</section>

<section class="postcard postcard--services">
  <div class="photo" role="img" aria-label="Photo of cupped hands holding coins with a small tree growing from them"></div>

  <svg style="position:absolute;left:0;top:0" width="470" height="313" aria-hidden="true">
    <path d="M0 0H217V38L196 62H0Z" fill="var(--lime)"/>
    <path d="M192 287L307 171H470V287Z" fill="var(--navy)"/>
  </svg>

  <h1 class="headline">Individualized Business and<br>Personal Accounting services<br>you can trust</h1>

  <div class="service-column">
    <div class="service">
      <h2 class="service-title">Tax Preparation</h2>
      <p class="service-text">With over 35 years of experience filing tax returns, we are experts in tax preparation. Including Personal Returns, Corporations, LLC's, Partnerships and State Franchise Tax Returns.</p>
    </div>
    <div class="service">
      <h2 class="service-title">Bookkeeping</h2>
      <p class="service-text">Let us take over the day-to-day bookkeeping so you can get back to running your business. We offer assistance with LedgerPro setup and provide ongoing bookkeeping services. Including frequent journal entries, accounts payables &amp; receivables, sales tax reporting &amp; payments, account reconciliation, and more.</p>
    </div>
    <div class="service">
      <h2 class="service-title">Financial Reporting</h2>
      <p class="service-text">We'll provide easy to understand financial reports that allow you and your team to manage cash flow, create budgets and make forecasting decisions. Depending on your needs, we can provide monthly, quarterly or yearly financial statements.</p>
    </div>
  </div>

  <div class="service service--payroll">
    <h2 class="service-title">Payroll Processing</h2>
    <p class="service-text">Whether you have 5 employees or 100+, payroll can be an overwhelming and time consuming task. We offer full-service payroll processing. Including employee onboarding, printed or direct deposit checks, quarterly payroll report filing, yearly W-2/W-3 and 1099 printing and filing, and more.</p>
  </div>

  <svg class="footer-band" viewBox="0 0 470 26" aria-hidden="true">
    <rect width="470" height="26" fill="var(--green)"/>
    <path d="M0 0H195C180 2 175 26 150 26H0Z" fill="var(--navy)"/>
  </svg>
  <div class="footer-url">www.harrowledgerworks.com</div>
</section>

</body>
</html>
```